Real Estate Flyer (Brenton Property)

We need a color CMYK high resolution, print quality horizontal real estate property flyer designed in the sizes of 10" wide and 6.7425" tall and another one in 11" wide and 8.5" tall.
Ad should be professionally looking to U.S. standards. It should be sleek, modern yet classy.
We uploaded in Briefs logo files, agent photo, 2 photos of the property (Must use both) and a sample of a flyer for Vayle Morrow Luxury Residence. We like how the overlay atop the first photo in the Vayle Morrow flyer with the company logo in the overlay. We'd like to incorporate that with our logo, the background color of the overlay should match that of our logo. DON'T CHANGE LOGO COLORS. Only use two colors in ad (exact logo blue color and white). The text in the overlay must be "FOR SALE - Potential Income Producing Commercial Office Building". Other details that should be prominent underneath are "42 Brenton Dr., Schaumburg, IL 60174 - Asking Price: $650,000".
Add "Residential & Commercial" under our company logo in italic font.
Add in flyer: "Located seconds away from the Kettering Rd. & Palden Rd. Intersection"
Add in flyer:
- Completely vacant
- 10,000 sq. ft. building
- 55 Car Parking
- 1.38 acre lot
- Over 20 offices and 5 bathrooms.
- Lease out individual office spaces for great monthly cash flow
Put agent's photo and following details professionally displayed:
Dev Marlo
Managing Broker
847-555-0148
dev.marlo@qtnhomes-example.com
Add from Briefs fair housing logo and PLX logo near agent's information. Logos should be small but yet visible to understand text.
Add at bottom of the ad with separation near agent details:
Looking to Buy or Sell?
I’m your one-stop, full service licensed real estate broker.
I deal with all types of real estate properties: Homes, Condos, Townhomes, Multi-Unit Apartment Buildings and Commercial Spaces.
Let My Experience Guide You Through Every Step of the Process!
Fine print:
©2018 QTN Homes, Inc. All Rights Reserved.

```html
<!DOCTYPE html>
<html lang="en">
<head>
<meta charset="utf-8">
<title>Brenton Property Flyer</title>
<link href="https://fonts.googleapis.com/css2?family=Montserrat:ital,wght@0,400;0,600;0,700;0,800;1,400&display=swap" rel="stylesheet">
<style>
  :root {
    --brand-blue: #2b4aa3;
    --brand-blue-dark: #223d8c;
    --white: #ffffff;
    --stage: #ececec;
    --photo-sky: #9fb6cf;
    --photo-building: #c9a98a;
    --photo-ground: #4d4b47;
  }
  * { margin: 0; padding: 0; box-sizing: border-box; }
  html, body { width: 809px; height: 1200px; overflow: hidden; }
  body {
    background: var(--stage);
    font-family: "Montserrat", Arial, sans-serif;
    color: var(--brand-blue);
    position: relative;
  }
  .flyer {
    position: absolute;
    left: 20px; top: 341px;
    width: 769px; height: 518px;
    background: var(--white);
    box-shadow: 0 2px 10px rgba(0,0,0,.15);
    display: grid;
    grid-template-columns: 250px 1fr;
    overflow: hidden;
  }
  /* left column */
  .side { display: flex; flex-direction: column; }
  .brand-panel {
    background: var(--brand-blue);
    color: var(--white);
    height: 190px;
    padding: 22px 18px 14px;
    text-align: center;
  }
  .brand-mark { display: flex; align-items: center; justify-content: center; gap: 10px; margin-top: 6px; }
  .brand-mark .square { width: 22px; height: 22px; background: var(--white); }
  .brand-mark .name { font-weight: 700; font-size: 30px; letter-spacing: 1px; }
  .tagline { font-style: italic; font-size: 12px; margin-top: 10px; }
  .location-note { font-size: 11px; line-height: 1.45; margin-top: 26px; }
  .features {
    list-style: none;
    text-align: center;
    font-size: 11px;
    line-height: 1.55;
    padding: 16px 14px;
    height: 140px;
  }
  .photo-secondary {
    flex: 1;
    margin: 0 0 0 0;
    background: linear-gradient(180deg, var(--photo-sky) 0%, #b7c4d2 40%, var(--photo-building) 62%, var(--photo-ground) 100%);
  }
  /* right column */
  .main { display: flex; flex-direction: column; border-left: 4px solid var(--white); }
  .photo-primary {
    height: 248px;
    background: linear-gradient(180deg, #8fb0d6 0%, #b9c9d8 38%, #d2ad83 60%, #3f3d3a 100%);
  }
  .sale-band {
    background: var(--brand-blue);
    color: var(--white);
    display: flex;
    align-items: center;
    justify-content: space-between;
    padding: 8px 16px;
    height: 74px;
  }
  .sale-band h1 { font-size: 38px; font-weight: 800; line-height: 1; letter-spacing: .5px; }
  .sale-band .subhead { font-size: 9px; margin-top: 5px; }
  .listing { text-align: right; font-size: 10px; line-height: 1.5; }
  .listing strong { font-weight: 700; }
  .agent {
    display: flex; align-items: center; gap: 14px;
    padding: 10px 16px;
    height: 104px;
  }
  .agent-photo {
    width: 62px; height: 80px;
    background: linear-gradient(180deg, #d9dde3, #8a96a8);
  }
  .agent-name { font-size: 24px; font-weight: 700; line-height: 1.1; }
  .agent-title { font-size: 11px; font-weight: 600; margin-bottom: 6px; }
  .contact { display: flex; align-items: center; gap: 7px; font-size: 11px; line-height: 1.6; }
  .contact svg { width: 11px; height: 11px; fill: var(--brand-blue); }
  .pitch {
    flex: 1;
    border-top: 2px solid var(--brand-blue);
    margin: 0 16px;
    padding: 8px 0;
    position: relative;
    font-size: 8.5px;
    line-height: 1.45;
    padding-right: 70px;
  }
  .pitch h2 { font-size: 11px; font-weight: 700; margin-bottom: 2px; }
  .pitch .closing { font-weight: 600; }
  .fine-print { font-size: 7px; margin-top: 3px; }
  .badges { position: absolute; right: 0; bottom: 10px; display: flex; gap: 6px; }
  .badge { width: 26px; height: 26px; background: var(--brand-blue); }
</style>
</head>
<body>
  <article class="flyer">
    <aside class="side">
      <div class="brand-panel">
        <div class="brand-mark"><span class="square"></span><span class="name">QTN Homes</span></div>
        <p class="tagline">Residential &amp; Commercial</p>
        <p class="location-note">Located seconds away from the<br>Kettering Rd. &amp; Palden Rd. Intersection</p>
      </div>
      <ul class="features">
        <li>Completely vacant</li>
        <li>10,000 sq. ft. building</li>
        <li>55 Car Parking</li>
        <li>1.38 acre lot</li>
        <li>Over 20 offices and 5 bathrooms.</li>
        <li>Lease out individual office spaces for great monthly cash flow</li>
      </ul>
      <div class="photo-secondary" role="img" aria-label="Photo of the office building from the side at dusk"></div>
    </aside>
    <section class="main">
      <div class="photo-primary" role="img" aria-label="Photo of the office building front with parking lot in evening light"></div>
      <div class="sale-band">
        <div>
          <h1>FOR SALE</h1>
          <p class="subhead">Potential Income Producing Commercial Office Building</p>
        </div>
        <div class="listing">
          <p>42 Brenton Dr., Schaumburg, IL 60174</p>
          <p><strong>Asking Price: $650,000</strong></p>
        </div>
      </div>
      <div class="agent">
        <div class="agent-photo" role="img" aria-label="Agent portrait"></div>
        <div>
          <p class="agent-name">Dev Marlo</p>
          <p class="agent-title">Managing Broker</p>
          <p class="contact"><svg viewBox="0 0 24 24"><path d="M6.6 10.8a15.1 15.1 0 0 0 6.6 6.6l2.2-2.2c.3-.3.7-.4 1-.2 1.1.4 2.3.6 3.6.6.6 0 1 .4 1 1V20c0 .6-.4 1-1 1C10.6 21 3 13.4 3 4c0-.6.4-1 1-1h3.5c.6 0 1 .4 1 1 0 1.3.2 2.5.6 3.6.1.3 0 .7-.2 1z"/></svg>847-555-0148</p>
          <p class="contact"><svg viewBox="0 0 24 24"><path d="M2 5h20v14H2zm2 2v.5l8 5 8-5V7zm0 2.9V17h16V9.9l-8 5z"/></svg>dev.marlo@qtnhomes-example.com</p>
        </div>
      </div>
      <div class="pitch">
        <h2>Looking to Buy or Sell?</h2>
        <p>I’m your one-stop, full service licensed real estate broker.</p>
        <p>I deal with all types of real estate properties: Homes, Condos, Townhomes, Multi-Unit Apartment Buildings and Commercial Spaces.</p>
        <p class="closing">Let My Experience Guide You Through Every Step of the Process!</p>
        <p class="fine-print">©2018 QTN Homes, Inc. All Rights Reserved.</p>
        <div class="badges"><span class="badge"></span><span class="badge"></span></div>
      </div>
    </section>
  </article>
</body>
</html>
```